SLides. Repair phone, tablet, pc, accessories seell and tempered glass.

i would like to show client what we do . what we sell. the repair can be done from 30min. We install tempered glasses. We sell accessories. have already slides. but design not very modern. need to change them. https://files.korvanet.example/share/7QxLm2PzR8TvWc4Hn9Kd https://files.korvanet.example/share/3JfTy6BnQ1XsVe8Ga5Lp i send all the design i have. our website is www.nutiparandus.ee i uploaded what photos i like.

Target Market(s)

Trade buy repair. phones, taböets, PC, sell accessories. show all services

Colors

Designer to choose colors to be used in the design.

Requirements
Must have
• modern design modern phone pictures. zelt pictures vorn pictures. To emphasize our style.
Nice to have
• modern pictures of our services. and modern pictures of goods.
Should not have
• non modern pictures and

```html
<!DOCTYPE html>
<html lang="en">
<head>
<meta charset="utf-8">
<title>Nutiparandus.ee — Repair slides</title>
<link href="https://fonts.googleapis.com/css2?family=Fira+Sans:wght@500;600&family=Lato:wght@900&display=swap" rel="stylesheet">
<style>
  :root {
    --stage: #000000;
    --amber: #fdb718;
    --ink: #111111;
    --white: #ffffff;
    --grey-desk: #a9a8a4;
    --grey-light: #b9b8b5;
    --tool-blue: #1f9fd6;
    --tool-navy: #0c3f62;
    --glove: #2a2d33;
  }
  * { box-sizing: border-box; margin: 0; padding: 0; }
  html, body {
    width: 1200px; height: 834px; overflow: hidden;
    background: var(--stage);
  }
  .canvas { position: relative; width: 1200px; height: 834px; }
  .slide {
    position: absolute; left: 95px; width: 1011px; height: 354px; overflow: hidden;
    font-family: "Fira Sans", sans-serif;
  }
  .slide--amber { top: 47px; background: var(--amber); }
  .slide--photo {
    top: 433px;
    background: linear-gradient(90deg, #9f9e9a 0%, var(--grey-desk) 50%, var(--grey-light) 100%);
  }
  .visual { position: absolute; top: 0; bottom: 0; right: 0; }
  .slide--amber .visual {
    left: 580px;
    background:
      linear-gradient(90deg, rgba(253,183,24,1) 0%, rgba(253,183,24,0) 22%),
      linear-gradient(160deg, #f4f6f7 0%, var(--tool-blue) 35%, #1587bd 60%, var(--tool-navy) 100%);
  }
  .slide--photo .visual {
    left: 480px;
    background:
      linear-gradient(90deg, rgba(169,168,164,1) 0%, rgba(169,168,164,0) 35%),
      linear-gradient(120deg, #8d8c89 0%, #5c5d60 35%, #e9e6df 55%, var(--glove) 80%, #1c1e23 100%);
  }
  .brand {
    position: absolute; left: 52px; top: 63px;
    display: flex; align-items: center; gap: 8px;
    font-weight: 500; font-size: 21px; line-height: 1; color: var(--ink); letter-spacing: -0.2px;
  }
  .brand__mark { width: 13px; height: 13px; border-radius: 50%; background: var(--ink); }
  .headline {
    position: absolute; left: 50px; top: 90px;
    font-family: "Lato", sans-serif; font-weight: 900; font-size: 43.5px; line-height: 1.1;
    color: var(--white); letter-spacing: -0.5px; white-space: nowrap;
  }
  .services { position: absolute; left: 52px; top: 150px; width: 440px; height: 80px; list-style: none; }
  .service {
    position: absolute; display: flex; align-items: center; gap: 12px;
    color: var(--white); font-size: 13px; font-weight: 500; white-space: nowrap;
  }
  .service__icon {
    width: 34px; height: 34px; border-radius: 50%;
    border: 1.5px solid rgba(255,255,255,0.85);
    display: flex; align-items: center; justify-content: center;
  }
  .service__icon svg { width: 16px; height: 16px; }
  .service--r1 { top: 0; } .service--r2 { top: 45px; }
  .service--c1 { left: 0; } .service--c2 { left: 245px; }
  .cta {
    position: absolute; left: 52px; top: 262px; width: 109px; height: 38px;
    display: flex; align-items: center; justify-content: center;
    font-weight: 600; font-size: 14.5px;
    border-bottom: 3px solid var(--ink);
  }
  .slide--amber .cta { background: var(--white); color: var(--ink); }
  .slide--photo .cta { background: var(--amber); color: var(--white); }
  .count {
    position: absolute; right: 14px; bottom: 8px;
    font-size: 10px; font-weight: 600; color: var(--ink);
  }
</style>
</head>
<body>
<main class="canvas">

  <section class="slide slide--amber">
    <div class="visual" role="img" aria-label="Flat illustration of a broken smartphone surrounded by screwdrivers, cables and screws"></div>
    <div class="brand"><span class="brand__mark"></span>Nutiparandus.ee</div>
    <h1 class="headline">Repair of Mobile Phone</h1>
    <ul class="services">
      <li class="service service--r1 service--c1">
        <span class="service__icon"><svg viewBox="0 0 16 16" fill="none" stroke="#111" stroke-width="2"><path d="M13 6a5 5 0 0 0-9-1.5M3 10a5 5 0 0 0 9 1.5"/><path d="M13 2v4H9M3 14v-4h4" stroke-width="1.6"/></svg></span>
        Motherboard replacement</li>
      <li class="service service--r1 service--c2">
        <span class="service__icon"><svg viewBox="0 0 16 16" fill="none" stroke="#111" stroke-width="1.8"><circle cx="8" cy="8" r="6"/><path d="M8 4.5V8H5.5"/></svg></span>
        Fast battery replacement</li>
      <li class="service service--r2 service--c1">
        <span class="service__icon"><svg viewBox="0 0 16 16" fill="none" stroke="#111" stroke-width="1.8"><rect x="4.5" y="1.5" width="7" height="13" rx="1.3"/><path d="M7 12.2h2"/></svg></span>
        Screen Swap</li>
      <li class="service service--r2 service--c2">
        <span class="service__icon"><svg viewBox="0 0 16 16" fill="#111"><path d="M10.5 1a4 4 0 0 0-3.7 5.4L1.3 11.9a1.4 1.4 0 0 0 2 2l5.5-5.5A4 4 0 0 0 14.6 4l-2.2 2.2-2-.6-.6-2L12 1.4A4 4 0 0 0 10.5 1z"/></svg></span>
        Heavy repair</li>
    </ul>
    <a class="cta">Find Us</a>
    <span class="count">x10</span>
  </section>

  <section class="slide slide--photo">
    <div class="visual" role="img" aria-label="Photo of gloved hands holding a cracked white smartphone beside a new phone, with repair tools on a grey desk"></div>
    <div class="brand"><span class="brand__mark"></span>Nutiparandus.ee</div>
    <h1 class="headline">Repair of Mobile Phone</h1>
    <ul class="services">
      <li class="service service--r1 service--c1">
        <span class="service__icon"><svg viewBox="0 0 16 16" fill="none" stroke="#111" stroke-width="2"><path d="M13 6a5 5 0 0 0-9-1.5M3 10a5 5 0 0 0 9 1.5"/><path d="M13 2v4H9M3 14v-4h4" stroke-width="1.6"/></svg></span>
        Motherboard replacement</li>
      <li class="service service--r1 service--c2">
        <span class="service__icon"><svg viewBox="0 0 16 16" fill="none" stroke="#111" stroke-width="1.8"><circle cx="8" cy="8" r="6"/><path d="M8 4.5V8H5.5"/></svg></span>
        Fast battery replacement</li>
      <li class="service service--r2 service--c1">
        <span class="service__icon"><svg viewBox="0 0 16 16" fill="none" stroke="#111" stroke-width="1.8"><rect x="4.5" y="1.5" width="7" height="13" rx="1.3"/><path d="M7 12.2h2"/></svg></span>
        Screen Swap</li>
      <li class="service service--r2 service--c2">
        <span class="service__icon"><svg viewBox="0 0 16 16" fill="#111"><path d="M10.5 1a4 4 0 0 0-3.7 5.4L1.3 11.9a1.4 1.4 0 0 0 2 2l5.5-5.5A4 4 0 0 0 14.6 4l-2.2 2.2-2-.6-.6-2L12 1.4A4 4 0 0 0 10.5 1z"/></svg></span>
        Heavy repair</li>
    </ul>
    <a class="cta">Find Us</a>
    <span class="count">x10</span>
  </section>

</main>
</body>
</html>
```